CFO services graphic design

I own a business consulting firm called Marlowe Consulting and we need a graphic for CFO services in our colours and branding. The attached file "CFO services to be put into Marlowe consulting theme", shows the content for the design. The two other files show the theme and colours for the new design.

```html
<!DOCTYPE html>
<html lang="en">
<head>
<meta charset="utf-8">
<title>CFO Services</title>
<link rel="stylesheet" href="https://fonts.googleapis.com/css2?family=Outfit:wght@400;500;800&display=swap">
<style>
  :root {
    --bg: #ffffff;
    --gap: #ffffff;
    --sky-light: #22aae3;
    --sky-deep: #1a83b2;
    --royal-light: #174fbd;
    --royal-deep: #123d8f;
    --navy-light: #10398a;
    --navy-deep: #0b2a60;
    --midnight-light: #0a2552;
    --midnight-deep: #061a3b;
    --orange-light: #f5921f;
    --orange-deep: #b4661a;
    --label: #ffffff;
    --title-shadow: #3a1f08;
  }
  html, body {
    margin: 0;
    padding: 0;
    width: 1200px;
    height: 1200px;
    overflow: hidden;
    background: var(--bg);
  }
  .cfo-wheel {
    display: block;
    width: 1200px;
    height: 1200px;
    font-family: "Outfit", sans-serif;
  }
  .petal { stroke: var(--gap); stroke-width: 30; }
  .hub { stroke: var(--gap); stroke-width: 60; }
  .petal-label {
    fill: var(--label);
    font-size: 35px;
    font-weight: 500;
    text-anchor: middle;
    dominant-baseline: middle;
  }
  .petal-label--small { font-size: 27px; }
  .hub-title {
    font-size: 60px;
    font-weight: 800;
    text-anchor: middle;
    dominant-baseline: middle;
  }
  .hub-title--face { fill: var(--label); }
  .hub-title--shadow { fill: var(--title-shadow); }
</style>
</head>
<body>
<svg class="cfo-wheel" viewBox="0 0 1932 1932" xmlns="http://www.w3.org/2000/svg" role="img" aria-label="Chief Financial Officer services wheel">
  <defs>
    <linearGradient id="grad-sky" x1="1" y1="0" x2="0" y2="1">
      <stop offset="0" stop-color="var(--sky-light)"/>
      <stop offset="1" stop-color="var(--sky-deep)"/>
    </linearGradient>
    <linearGradient id="grad-sky-up" x1="0" y1="1" x2="1" y2="0">
      <stop offset="0" stop-color="var(--sky-light)"/>
      <stop offset="1" stop-color="var(--sky-deep)"/>
    </linearGradient>
    <linearGradient id="grad-royal" x1="1" y1="0" x2="0" y2="1">
      <stop offset="0" stop-color="var(--royal-light)"/>
      <stop offset="1" stop-color="var(--royal-deep)"/>
    </linearGradient>
    <linearGradient id="grad-royal-left" x1="0" y1="1" x2="1" y2="0">
      <stop offset="0" stop-color="var(--royal-light)"/>
      <stop offset="1" stop-color="var(--royal-deep)"/>
    </linearGradient>
    <linearGradient id="grad-navy" x1="0" y1="0" x2="1" y2="0">
      <stop offset="0" stop-color="var(--navy-light)"/>
      <stop offset="1" stop-color="var(--navy-deep)"/>
    </linearGradient>
    <linearGradient id="grad-midnight" x1="0" y1="0" x2="0" y2="1">
      <stop offset="0" stop-color="var(--midnight-light)"/>
      <stop offset="1" stop-color="var(--midnight-deep)"/>
    </linearGradient>
    <linearGradient id="grad-orange" x1="1" y1="0" x2="0" y2="1">
      <stop offset="0" stop-color="var(--orange-light)"/>
      <stop offset="1" stop-color="var(--orange-deep)"/>
    </linearGradient>
    <clipPath id="clip-right-half">
      <rect x="966" y="0" width="966" height="1932"/>
    </clipPath>
  </defs>

  <!-- petals, each layered over its clockwise neighbour -->
  <g class="petals">
    <circle class="petal petal--cost" cx="970" cy="484" r="211" fill="url(#grad-sky)"/>
    <circle class="petal petal--communication" cx="625" cy="625" r="211" fill="url(#grad-midnight)"/>
    <circle class="petal petal--compliance" cx="484" cy="966" r="211" fill="url(#grad-navy)"/>
    <circle class="petal petal--risk" cx="625" cy="1307" r="211" fill="url(#grad-royal-left)"/>
    <circle class="petal petal--budgeting" cx="966" cy="1448" r="211" fill="url(#grad-sky-up)"/>
    <circle class="petal petal--performance" cx="1307" cy="1307" r="211" fill="url(#grad-midnight)"/>
    <circle class="petal petal--investment" cx="1448" cy="966" r="211" fill="url(#grad-navy)"/>
    <circle class="petal petal--capital" cx="1307" cy="625" r="211" fill="url(#grad-royal)"/>
    <circle class="petal petal--cost" cx="970" cy="484" r="211" fill="url(#grad-sky)" clip-path="url(#clip-right-half)"/>
  </g>

  <circle class="hub" cx="966" cy="966" r="302" fill="url(#grad-orange)"/>

  <g class="labels">
    <text class="petal-label" x="982" y="416">Cost Accounting</text>
    <text class="petal-label" x="982" y="452">&amp; Cost</text>
    <text class="petal-label" x="982" y="488">Management</text>

    <text class="petal-label" x="1336" y="556">Capital</text>
    <text class="petal-label" x="1336" y="592">Structure</text>
    <text class="petal-label" x="1336" y="629">and the</text>
    <text class="petal-label" x="1336" y="665">Cost of Capital</text>

    <text class="petal-label" x="1479" y="941">Long-term &amp;</text>
    <text class="petal-label" x="1479" y="977">Short-term</text>
    <text class="petal-label" x="1479" y="1013">Investment</text>
    <text class="petal-label" x="1479" y="1049">Decisions</text>

    <text class="petal-label" x="1313" y="1323">Performance</text>
    <text class="petal-label" x="1313" y="1359">Evaluation</text>

    <text class="petal-label" x="949" y="1446">Budgeting &amp;</text>
    <text class="petal-label" x="949" y="1482">Strategic</text>
    <text class="petal-label" x="949" y="1518">Planning</text>

    <text class="petal-label" x="596" y="1282">Risk</text>
    <text class="petal-label" x="596" y="1318">Management</text>

    <text class="petal-label" x="453" y="911">Compliance:</text>
    <text class="petal-label" x="453" y="947">Tax, Legal and</text>
    <text class="petal-label" x="453" y="984">Regulatory</text>

    <text class="petal-label" x="625" y="528">Communication:</text>
    <text class="petal-label petal-label--small" x="625" y="561">Board of Directors,</text>
    <text class="petal-label petal-label--small" x="625" y="591">Creditors, Owners,</text>
    <text class="petal-label petal-label--small" x="625" y="621">Investors, Credit</text>
    <text class="petal-label petal-label--small" x="625" y="652">Rating Agencies</text>
  </g>

  <g class="hub-heading">
    <text class="hub-title hub-title--shadow" x="962" y="942" textLength="430" lengthAdjust="spacingAndGlyphs">CHIEF FINANCIAL</text>
    <text class="hub-title hub-title--shadow" x="962" y="1000" textLength="212" lengthAdjust="spacingAndGlyphs">OFFICER</text>
    <text class="hub-title hub-title--face" x="966" y="938" textLength="430" lengthAdjust="spacingAndGlyphs">CHIEF FINANCIAL</text>
    <text class="hub-title hub-title--face" x="966" y="996" textLength="212" lengthAdjust="spacingAndGlyphs">OFFICER</text>
  </g>
</svg>
</body>
</html>
```